Flyer for the Harvest of Lanterns Conference

Flyer design for an annual international conference called "MERIVAL 2017". This is a conference for young adults, so we hope to produce a design that is both professional and appealing to young people in general

We'd like the flyer to showcase the conference brand logo, and clearly highlight the key information to people who will read it.

Target Market(s)

Young people, young adults

Industry/Entity Type

Religious

Font styles to use
Sans Serif

Colors

Designer to choose colors to be used in the design.

Requirements
Must have
• - Should be only one page (Vertical or Horizontal).
• - the MERVAL logo and all the information found in the attached text file. This includes: Main topic: Your sons and daughters shall prophesy,
• Dates and time, location, contact information and everything that is in the attached text file.
Nice to have
• It would be nice to see samples where the white logo is used and another where the black one is used.
Should not have
• This is NOT a folded flyer, we will be sticking it on doors and public places. And we will be printing large simple to put on walls. So only one page with few words like an add (the words are in the attached file)

```html
<!DOCTYPE html>
<html lang="en">
<head>
<meta charset="utf-8">
<title>MERIVAL 2017 – Harvest of Lanterns Conference</title>
<link href="https://fonts.googleapis.com/css2?family=Lato:wght@400;700;900&display=swap" rel="stylesheet">
<style>
  :root {
    --backdrop: #58585a;
    --orange: #f7941d;
    --orange-deep: #e8801a;
    --gold: #f5c518;
    --ink: #2b2b2b;
    --panel: #e6e7e8;
    --paper: #ffffff;
    --sky-dark: #1a0f08;
    --sky-mid: #5a3219;
    --sky-glow: #a8622a;
  }
  * { box-sizing: border-box; margin: 0; padding: 0; }
  html, body { width: 800px; height: 1200px; overflow: hidden; }
  body {
    background: var(--backdrop);
    font-family: "Lato", Arial, sans-serif;
    position: relative;
  }
  .flyer {
    position: absolute;
    left: 20px; top: 62px;
    width: 760px; height: 1075px;
    background: var(--paper);
    overflow: hidden;
  }
  .hero {
    position: absolute; left: 0; top: 0;
    width: 760px; height: 464px;
    background:
      radial-gradient(ellipse at 65% 55%, var(--sky-glow) 0%, rgba(168,98,42,0) 55%),
      linear-gradient(180deg, var(--sky-dark) 0%, var(--sky-mid) 45%, #3a200f 72%, #000 86%, #000 100%);
  }
  .brand {
    position: absolute; left: 36px; top: 30px;
    width: 150px; text-align: center;
  }
  .brand-mark {
    display: block; margin: 0 auto 8px;
  }
  .brand-name {
    color: var(--paper);
    font-weight: 700; font-size: 24px; letter-spacing: 3px;
  }
  .event-title {
    position: absolute; left: 0; right: 0; top: 375px;
    text-align: center; color: var(--gold);
    font-weight: 900; font-size: 56px; line-height: 1;
  }
  .event-subtitle {
    position: absolute; left: 0; right: 0; top: 424px;
    text-align: center; color: var(--gold);
    font-weight: 700; font-size: 33px; line-height: 1;
  }
  .theme-band {
    position: absolute; left: 0; top: 464px;
    width: 760px; height: 120px;
    background: var(--orange);
    display: flex; align-items: center; justify-content: center;
    text-align: center; color: var(--paper);
    font-weight: 900; font-size: 42px; line-height: 1.12;
    text-transform: uppercase;
    text-shadow: 2px 2px 3px rgba(0,0,0,0.45);
  }
  .body-fade {
    position: absolute; left: 0; top: 584px;
    width: 760px; height: 428px;
    background: linear-gradient(180deg, #ffffff 0%, #ffffff 60%, #d9d9da 100%);
  }
  .speakers {
    position: absolute; left: 48px; top: 664px;
  }
  .speakers h2 {
    color: var(--orange); font-weight: 700; font-size: 29px;
    margin-bottom: 16px;
  }
  .speaker-list { list-style: none; }
  .speaker-list li {
    display: flex; align-items: center;
    height: 49px;
    font-weight: 700; font-size: 19px; color: var(--ink);
  }
  .speaker-list svg { margin-right: 14px; flex: none; }
  .details {
    position: absolute; left: 402px; top: 630px;
    width: 358px; height: 345px;
    background: var(--panel);
    border-radius: 30px 0 0 30px;
    padding: 34px 20px 0 38px;
  }
  .detail { margin-bottom: 17px; }
  .detail-label {
    color: var(--orange); font-size: 16px; line-height: 1.2;
  }
  .detail-value {
    color: var(--ink); font-weight: 700; font-size: 17px; line-height: 1.3;
  }
  .contact-bar {
    position: absolute; left: 0; top: 1012px;
    width: 760px; height: 63px;
    background: var(--orange-deep);
    display: flex; align-items: center; justify-content: center;
    color: var(--paper); font-weight: 700; font-size: 16px;
  }
</style>
</head>
<body>
  <main class="flyer">
    <section class="hero" role="img" aria-label="Dramatic sunset sky with a silhouetted young man raising his arms beside a wooden cross draped in cloth">
    </section>

    <div class="brand">
      <svg class="brand-mark" width="64" height="64" viewBox="0 0 64 64" aria-hidden="true">
        <circle cx="32" cy="32" r="29" fill="none" stroke="var(--orange)" stroke-width="3"/>
      </svg>
      <span class="brand-name">MERVAL</span>
    </div>

    <h1 class="event-title">MERIVAL 2017</h1>
    <p class="event-subtitle">HARVEST OF LANTERNS CONFERENCE</p>

    <div class="theme-band">Your sons and daughters<br>shall prophesy</div>

    <div class="body-fade"></div>

    <section class="speakers">
      <h2>Speakers:</h2>
      <ul class="speaker-list">
        <li><svg width="16" height="16" viewBox="0 0 16 16" aria-hidden="true"><circle cx="8" cy="8" r="6.5" fill="none" stroke="var(--orange)" stroke-width="1.4"/><path d="M4.8 8.2l2.3 2.2 4.8-5" fill="none" stroke="var(--orange)" stroke-width="1.6"/></svg>Prophet Lucien Marowa</li>
        <li><svg width="16" height="16" viewBox="0 0 16 16" aria-hidden="true"><circle cx="8" cy="8" r="6.5" fill="none" stroke="var(--orange)" stroke-width="1.4"/><path d="M4.8 8.2l2.3 2.2 4.8-5" fill="none" stroke="var(--orange)" stroke-width="1.6"/></svg>Bishop Samuel Otenga</li>
        <li><svg width="16" height="16" viewBox="0 0 16 16" aria-hidden="true"><circle cx="8" cy="8" r="6.5" fill="none" stroke="var(--orange)" stroke-width="1.4"/><path d="M4.8 8.2l2.3 2.2 4.8-5" fill="none" stroke="var(--orange)" stroke-width="1.6"/></svg>Prophet Nathan Liu Mbeki</li>
        <li><svg width="16" height="16" viewBox="0 0 16 16" aria-hidden="true"><circle cx="8" cy="8" r="6.5" fill="none" stroke="var(--orange)" stroke-width="1.4"/><path d="M4.8 8.2l2.3 2.2 4.8-5" fill="none" stroke="var(--orange)" stroke-width="1.6"/></svg>Prophet Andre Kilolo</li>
        <li><svg width="16" height="16" viewBox="0 0 16 16" aria-hidden="true"><circle cx="8" cy="8" r="6.5" fill="none" stroke="var(--orange)" stroke-width="1.4"/><path d="M4.8 8.2l2.3 2.2 4.8-5" fill="none" stroke="var(--orange)" stroke-width="1.6"/></svg>Prophet Isaac</li>
      </ul>
    </section>

    <aside class="details">
      <div class="detail">
        <p class="detail-label">Senga Date:</p>
        <p class="detail-value">September 1st, 2nd and 3rd 2017</p>
      </div>
      <div class="detail">
        <p class="detail-label">Start Time:</p>
        <p class="detail-value">6:00PM</p>
      </div>
      <div class="detail">
        <p class="detail-label">Location:</p>
        <p class="detail-value">Brookfield Lantern Hall Inn<br>415 Harbor Lane<br>Westbrook, ME 04092 United</p>
      </div>
      <div class="detail">
        <p class="detail-label">States Room:</p>
        <p class="detail-value">Maple Grove Ballroom</p>
      </div>
    </aside>

    <footer class="contact-bar">
      Tel:+1 (555) 014 2290 | Email:hello@lanternharvest.org | Website: http://merval-events.org
    </footer>
  </main>
</body>
</html>
```